I need a new business card design for my pharmacy.

I need a business card design. I will include my logo.
The card needs to be readable. I prefer to have my logo on one side along with my website, the other side includes the other information. Please use combination of black, neon green, white, and silver. This needs to catch the eye but yet be clearly visible and legible. Thanks

Industry/Entity Type

Pharmacy

Contact Information for Business Card

It needs to have the following information listed:
Mel's Apothecary Owner/Pharm D.
7134 North Brook Lane
Sioux Falls, SD 57231
Phone 605-318-6207
Fax 605-318-6209
email: mel@melsapothecary-example.com
www.melsapothecary-example.com
Store hours Monday-Friday 8 am- 7 pm
Saturday 8 am- 12 pm
Sunday Closed
Please utilize the colors black, white, and neon green, maybe silver.

Requirements
Must have
• It needs to be easily readable!
Nice to have
• It should catch the eye.
Should not have
• Do not use any other colors except listed: black, neon green, white, & silver.

```html
<!DOCTYPE html>
<html lang="en">
<head>
<meta charset="utf-8">
<title>Mel's Apothecary – Business Card</title>
<link href="https://fonts.googleapis.com/css2?family=Open+Sans:wght@400;600;700&display=swap" rel="stylesheet">
<style>
  :root {
    --bg: #2b2b2b;
    --black: #1c1b1c;
    --ink: #1e1e1e;
    --neon: #a6cf2f;
    --neon-light: #bde03c;
    --white: #ffffff;
    --silver: #d9d9d9;
    --grey-text: #333333;
  }
  * { margin: 0; padding: 0; box-sizing: border-box; }
  html, body { width: 1200px; height: 834px; overflow: hidden; }
  body {
    background: var(--bg);
    font-family: "Open Sans", Arial, sans-serif;
    position: relative;
  }
  .card {
    position: absolute;
    width: 600px;
    height: 343px;
    box-shadow: 0 14px 30px rgba(0,0,0,.45);
  }
  /* Front side */
  .card-front {
    left: 60px; top: 66px;
    background: var(--black);
  }
  .brand {
    position: absolute;
    display: flex;
    align-items: center;
    gap: 22px;
  }
  .brand-dot {
    width: 52px; height: 52px;
    border-radius: 50%;
    background: var(--neon);
  }
  .brand-rule {
    width: 2px; height: 74px;
  }
  .brand-name {
    font-weight: 600;
    font-size: 38px;
    letter-spacing: -1px;
    white-space: nowrap;
  }
  .card-front .brand { left: 76px; top: 92px; }
  .card-front .brand-rule { background: var(--silver); }
  .card-front .brand-name { color: var(--white); }
  .front-band {
    position: absolute;
    left: 0; right: 0; top: 232px;
    height: 38px;
    background: linear-gradient(90deg, var(--neon-light), var(--neon));
    display: flex; align-items: center; justify-content: center;
  }
  .front-url {
    font-size: 14px;
    color: var(--ink);
    letter-spacing: .3px;
  }
  /* Back side */
  .card-back {
    left: 540px; top: 425px;
    background: linear-gradient(135deg, var(--white) 0%, #f2f2f2 55%, var(--silver) 100%);
  }
  .card-back .brand { left: 64px; top: 44px; }
  .card-back .brand-rule { background: var(--ink); }
  .card-back .brand-name { color: var(--ink); }
  .back-rule {
    position: absolute;
    left: 64px; right: 40px;
    height: 1px;
    background: var(--ink);
  }
  .back-rule.top { top: 140px; left: 240px; }
  .back-rule.bottom { top: 268px; }
  .contact {
    position: absolute;
    left: 64px; right: 40px; top: 156px;
    text-align: center;
    color: var(--grey-text);
  }
  .role { font-size: 17px; font-weight: 700; color: var(--ink); }
  .role .accent { font-weight: 400; color: var(--neon); }
  .address { font-size: 14px; margin-top: 6px; }
  .lines {
    display: flex; justify-content: center; align-items: center; gap: 16px;
    font-size: 13.5px; margin-top: 6px;
  }
  .lines span { display: inline-flex; align-items: center; gap: 5px; }
  .lines svg { width: 14px; height: 14px; fill: none; stroke: var(--neon); stroke-width: 1.8; }
  .web { font-size: 15px; margin-top: 6px; }
  .web .accent { color: var(--neon); }
</style>
</head>
<body>
  <section class="card card-front" aria-label="Card front">
    <div class="brand">
      <div class="brand-dot"></div>
      <div class="brand-rule"></div>
      <div class="brand-name">Mel's Apothecary</div>
    </div>
    <div class="front-band">
      <span class="front-url">www.melsapothecary-example.com</span>
    </div>
  </section>

  <section class="card card-back" aria-label="Card back">
    <div class="brand">
      <div class="brand-dot"></div>
      <div class="brand-rule"></div>
      <div class="brand-name">Mel's Apothecary</div>
    </div>
    <div class="back-rule top"></div>
    <div class="contact">
      <p class="role">Pharm D. - <span class="accent">Owner</span></p>
      <p class="address">7134 North Brook Lane Sioux Falls, SD 57231</p>
      <p class="lines">
        <span>
          <svg viewBox="0 0 16 16" aria-hidden="true"><path d="M2 6c0-2 3-3 6-3s6 1 6 3l-3 1-1-2H6L5 7 2 6z"/><path d="M4 8h8l1 5H3l1-5z"/></svg>
          605-318-6207
        </span>
        <span>
          <svg viewBox="0 0 16 16" aria-hidden="true"><rect x="4" y="2" width="8" height="5"/><rect x="2" y="7" width="12" height="6"/></svg>
          605-318-6209
        </span>
        <span>
          <svg viewBox="0 0 16 16" aria-hidden="true"><rect x="2" y="4" width="12" height="9"/><path d="M2 4l6 5 6-5"/></svg>
          mel@melsapothecary-example.com
        </span>
      </p>
      <p class="web">www.melsapothecary-example<span class="accent">.com</span></p>
    </div>
    <div class="back-rule bottom"></div>
  </section>
</body>
</html>
```